Anzeigengestaltung für Zahnarztpraxis
Zielgruppe
Zahnarztpraxis
Aufgabenstellung
Möchte eine moderne Stellenanzeige, ggf. einen zum Logo farblich passenden Rahmen; ggf. noch mit Bildern

```html
<!DOCTYPE html>
<html lang="de">
<head>
<meta charset="utf-8">
<title>Stellenanzeige Zahnarztpraxis Talheim</title>
<link href="https://fonts.googleapis.com/css2?family=Poppins:wght@400;500;600;700&display=swap" rel="stylesheet">
<style>
  :root {
    --navy: #364c78;
    --green: #8dbb47;
    --paper: #eeeff2;
    --band: #e1e2e7;
    --text: #3e4048;
    --frame: #8a8c93;
    --white: #ffffff;
  }
  * { margin: 0; padding: 0; box-sizing: border-box; }
  html, body { width: 1200px; height: 1141px; overflow: hidden; background: var(--white); }
  body { font-family: "Poppins", sans-serif; color: var(--text); }

  .ad {
    position: relative;
    width: 1200px; height: 1141px;
    background: var(--paper);
    overflow: hidden;
  }
  .ad__frame {
    position: absolute; inset: 0 30px 30px 30px;
    border: 1px solid var(--frame);
    border-top: none;
    pointer-events: none;
    z-index: 3;
  }

  /* Header */
  .header { position: absolute; top: 0; left: 0; right: 0; height: 300px; }
  .header__brand {
    position: absolute; top: 0; left: 0; width: 790px; height: 300px;
    background: var(--navy);
    display: flex; align-items: center; gap: 26px;
    padding-left: 95px;
  }
  .brand__mark {
    width: 112px; height: 112px; border-radius: 50%;
    border: 12px solid var(--white);
    flex: none;
  }
  .brand__name {
    font-weight: 500; font-size: 38px; line-height: 1.05;
    color: var(--white);
  }
  .header__callout {
    position: absolute; top: 0; right: 0; width: 410px; height: 300px;
    background: var(--green);
    display: flex; align-items: center; justify-content: center;
    text-align: center;
    font-weight: 700; font-size: 34px; line-height: 1.2;
    letter-spacing: 1.5px; text-transform: uppercase;
  }
  .callout__top { color: var(--white); display: block; }
  .callout__bottom { color: var(--navy); display: block; }

  /* Intro */
  .intro { position: absolute; top: 335px; left: 85px; right: 60px; }
  .intro__lead {
    color: var(--green); font-weight: 600; font-size: 23px;
    letter-spacing: 2px; text-transform: uppercase;
  }
  .intro__roles { margin-top: 14px; }
  .intro__role {
    display: block;
    color: var(--navy); font-weight: 600; font-size: 37px; line-height: 1.25;
  }

  /* Columns */
  .section-title {
    color: var(--navy); font-weight: 600; font-size: 23px; line-height: 35px;
    letter-spacing: 1px; text-transform: uppercase;
    margin-bottom: 22px;
  }
  .checklist { list-style: none; }
  .checklist__item {
    display: flex; gap: 16px;
    font-size: 19px; line-height: 27px; color: var(--text);
    letter-spacing: 0.4px;
  }
  .checklist__tick { flex: none; width: 24px; height: 16px; margin-top: 4px; }
  .benefits { position: absolute; top: 500px; left: 85px; width: 480px; }
  .values { position: absolute; top: 580px; left: 630px; width: 520px; }
  .values .checklist__item { margin-bottom: 6px; }
  .values__closing {
    margin-top: 18px; color: var(--navy);
    font-weight: 600; font-size: 20px; line-height: 28px;
  }

  /* Footer */
  .footer {
    position: absolute; left: 0; right: 0; bottom: 0; height: 250px;
    background: var(--band);
    padding: 40px 0 0 85px;
  }
  .footer__text { width: 760px; font-size: 19px; line-height: 1.5; letter-spacing: 0.3px; }
  .footer__hook { color: var(--navy); font-weight: 700; font-size: 32px; }
  .footer__sep { color: var(--green); margin: 0 4px; }
  .footer__mail { white-space: nowrap; }
  .cta {
    position: absolute; right: 130px; bottom: 40px;
    width: 190px; height: 190px; border-radius: 50%;
    background: var(--navy);
    display: flex; flex-direction: column; align-items: center; justify-content: center;
    font-weight: 700; font-size: 24px; line-height: 1.15; letter-spacing: 1.5px;
    text-transform: uppercase; color: var(--white);
    z-index: 2;
  }
  .cta__accent { color: var(--green); }
</style>
</head>
<body>
<svg width="0" height="0" style="position:absolute">
  <defs>
    <symbol id="tick" viewBox="0 0 24 16">
      <path d="M2 8 L9 14 L22 2" fill="none" stroke="#8dbb47" stroke-width="3.5" stroke-linecap="round" stroke-linejoin="round"/>
    </symbol>
  </defs>
</svg>

<main class="ad">
  <header class="header">
    <div class="header__brand">
      <span class="brand__mark" aria-hidden="true"></span>
      <span class="brand__name">Zahnarztpraxis<br>Talheim</span>
    </div>
    <div class="header__callout">
      <p><span class="callout__top">Verstärkung</span><span class="callout__bottom">gesucht!</span></p>
    </div>
  </header>

  <section class="intro">
    <p class="intro__lead">Zur Erweiterung unseres Teams suchen wir:</p>
    <h1 class="intro__roles">
      <span class="intro__role">Zahnmedizinische Fachangestellte (m,w,d)</span>
      <span class="intro__role">Zahnmedizinische Prophylaxeassistentin (m,w,d)</span>
    </h1>
  </section>

  <section class="benefits">
    <h2 class="section-title">Deine Vorteile:</h2>
    <ul class="checklist">
      <li class="checklist__item"><svg class="checklist__tick"><use href="#tick"/></svg>Geregelte Arbeitszeiten</li>
      <li class="checklist__item"><svg class="checklist__tick"><use href="#tick"/></svg>Top moderne Ausstattung</li>
      <li class="checklist__item"><svg class="checklist__tick"><use href="#tick"/></svg>Spannende Mitarbeiterevents</li>
      <li class="checklist__item"><svg class="checklist__tick"><use href="#tick"/></svg>Etabliertes Qualitätsmanagement und klare Strukturen</li>
      <li class="checklist__item"><svg class="checklist__tick"><use href="#tick"/></svg>Flexible Urlaubsplanung</li>
      <li class="checklist__item"><svg class="checklist__tick"><use href="#tick"/></svg>Sehr gute Gehalts- und Weiterbildungsmöglichkeiten</li>
      <li class="checklist__item"><svg class="checklist__tick"><use href="#tick"/></svg>Kostenfreie Zahnbehandlungen inkl. Bleaching</li>
    </ul>
  </section>

  <section class="values">
    <h2 class="section-title">Was uns wichtig ist:</h2>
    <ul class="checklist">
      <li class="checklist__item"><svg class="checklist__tick"><use href="#tick"/></svg>Du bist aufgeschlossen<br>und motiviert</li>
      <li class="checklist__item"><svg class="checklist__tick"><use href="#tick"/></svg>Du bist kommunikativ und<br>kontaktfreudig im Umgang<br>mit Menschen</li>
      <li class="checklist__item"><svg class="checklist__tick"><use href="#tick"/></svg>Du hast Freude an deiner Arbeit</li>
    </ul>
    <p class="values__closing">Dann bist DU die Verstärkung,<br>die wir suchen!</p>
  </section>

  <footer class="footer">
    <p class="footer__text">
      <span class="footer__hook">Interesse?</span> Wir freuen uns über eine schriftliche
      Bewerbung per Post an: Dr. Harbeck<span class="footer__sep">|</span>Lindenstr. 12<span class="footer__sep">|</span>
      73460 Talheim oder per Mail an: <span class="footer__mail">timo-harbeck@postfeld.de</span>
    </p>
  </footer>

  <div class="cta"><span>Bewirb</span><span>dich</span><span class="cta__accent">jetzt!</span></div>

  <div class="ad__frame" aria-hidden="true"></div>
</main>
</body>
</html>
```